I need business cards for a company that will be an umbrella for many retail stores. I need them to be sleek and modern. I would like some white and black in the background of the card as these are the office colours the logo is attached.
Target Market(s)
worldwide
Industry/Entity Type
Business
Requirements
Must have
- traditional business card shape
Should not have
- too many colours
no swirly text

```html
<!DOCTYPE html>
<html lang="en">
<head>
<meta charset="utf-8">
<title>Orla General Trading – Business Card</title>
<link rel="stylesheet" href="https://fonts.googleapis.com/css2?family=Open+Sans:wght@400;600;700&display=swap">
<style>
  :root {
    --paper: #ffffff;
    --band: #000000;
    --band-text: #ffffff;
    --brand-ink: #1a1a1a;
    --mark-grey: #9a9a9a;
    --rule-grey: #e6e6e6;
  }
  html, body {
    margin: 0;
    padding: 0;
    width: 1200px;
    height: 634px;
    overflow: hidden;
    background: var(--paper);
  }
  .card {
    position: relative;
    width: 1200px;
    height: 634px;
    background: var(--paper);
    font-family: "Open Sans", Tahoma, sans-serif;
  }
  .brand-mark {
    position: absolute;
    left: 108px;
    top: 74px;
    width: 96px;
    height: 96px;
    border-radius: 50%;
    background: var(--mark-grey);
  }
  .brand-name {
    position: absolute;
    left: 236px;
    top: 99px;
    margin: 0;
    color: var(--brand-ink);
    font-weight: 600;
    font-size: 32px;
    line-height: 44px;
    letter-spacing: 0.5px;
    white-space: nowrap;
  }
  .header-rule {
    position: absolute;
    left: 236px;
    top: 200px;
    width: 880px;
    height: 3px;
    background: linear-gradient(to right, var(--rule-grey), rgba(230,230,230,0));
  }
  .contact-band {
    position: absolute;
    left: 18px;
    top: 268px;
    width: 1150px;
    height: 346px;
    background: var(--band);
    color: var(--band-text);
  }
  .contact-band p {
    position: absolute;
    margin: 0;
    white-space: nowrap;
    line-height: 1.2;
  }
  .owner-name  { left: 134px; top: 36px; font-size: 23px; font-weight: 700; }
  .owner-title { left: 134px; top: 74px; font-size: 23px; font-weight: 700; }
  .phone   { left: 134px; top: 155px; font-size: 21px; }
  .fax     { left: 415px; top: 152px; font-size: 21px; }
  .email   { left: 134px; top: 205px; font-size: 21px; }
  .website { left: 417px; top: 200px; font-size: 21px; }
  .address { left: 138px; top: 256px; font-size: 20px; }
</style>
</head>
<body>
  <div class="card">
    <header class="brand">
      <div class="brand-mark" aria-hidden="true"></div>
      <h1 class="brand-name">Orla General Trading</h1>
      <div class="header-rule" aria-hidden="true"></div>
    </header>
    <section class="contact-band">
      <p class="owner-name">Name of Business Owner</p>
      <p class="owner-title">Title of owner</p>
      <p class="phone">Phone : 000.000.0000</p>
      <p class="fax">Faxl: 000.000.0000</p>
      <p class="email">owner@orlagt.com</p>
      <p class="website">www.orlagt.com</p>
      <p class="address">complete address of the Retail owner plus the P.O. Box numbedr in one line</p>
    </section>
  </div>
</body>
</html>
```